International Health Supplement Company Needs Packaging and Label Redesign

Copper Lantern LLC requires a redesign for 1 internationally sold product and accompanying designs for 5 additional products. The additional products are currently sold locally and yet to be released internationally.

Our company is honest, premium, and passionate about supplements. We adopt a 'no BS' stance and as such source only the finest ingredients and deliver high-quality liquid health supplements to customers globally. We do not compromise on quality and do not apologise for price.

We want a clean, crisp design that conveys ‘premium, cutting-edge, boutique’ at a glance. We feel our current design appeals more to the 'chest beaters' rather than the 'chess players' that our research has indicated are our customers.

We have SIX PRODUCTS TOTAL in our range and feel individual color cues to distinguish the different products would greatly assist customer navigation i.e. Customers will identify ‘red’ means ‘product X’ without reading the label. (Examples attached and below we believe do this well).

Current 30ml bottle, cap, and dropper are in black and will remain so. Current label is black, however, we have a white label on our local product (example attached) and prefer the look of it.

Packaging is currently black and could remain so however most products that appeal to our target market are in white with color accents.

One consideration we have is that the product up until now has been selling exceptionally well so we need to retain some kind of familiarity with the existing branding. Perhaps that’s just the logo.

Logo can be revised i.e. add company name and/or company slogan.

Products are: (Function - Name)

Testosterone Support - Tongkat Ali (current)
Hormone Support - Jiaogulan
Energy Support - Ashwaghanda
Libido Support - Krachai Dam (for men)
Libido Support - Kacip Fatimah (for women)
Sleep Support - Wild Chamomile

Packaging: 4.6cm (L) x 8.0cm (W) x 11.2cm (H)
Label: 30 mL bottle

https://www.folioweb.example/gallery/TONIC-BOX-STUDY-2011/7402518
http://www.pelkastudio.example/projects/#/river-tea/
https://www.folioweb.example/gallery/31420786/Velmora-Skin
https://au.pinboardly.example/pin/592719083317915736/
https://au.pinboardly.example/pin/36916877689752218/
http://velto.example/en/portfolio/logo-redesign/

Target Market(s)

Generation X Men (and their partners), 36-55, upper middle class, who appreciate quality products.

Industry/Entity Type

Health Product

Font styles to use
Serif
Sans Serif

Requirements
Must have
• Packaging - Principal Display Panel (Front):
• 1. Function & Name of each product i.e 'Testosterone Support' & 'Tongkat Ali'
• 2. '30ml' AND '1 fl oz' (text size 1.8in / 3.2mm / 9 point min.)
• 3. 'Dietary Supplement'
• Packaging - Information Panel (Right):
• 1. Supplement Facts Panel (template accepted for drafts)
• 2. Directions: (lorum ipsum accepted for drafts)
• 3. Safety Warning: (lorum ipsum accepted for drafts)
• 4. 'Manufactured for: Copper Lantern LLC'
• 5. 'Sheridan, Wyoming'
• 6. '(414) 563 2180'
• 7. 'Product of Thailand'
• Bottle Label:
• 3. 'Dietary Supplement'
• 4. Supplement Facts Panel (template accepted for drafts)
• 5. Directions: (lorum ipsum accepted for drafts)
• 6. Safety Warning: (forum ipsum accepted for drafts)
• 7. 'Manufactured for: Copper Lantern LLC'
• 8. 'Sheridan, Wyoming'
• 9. '(414) 563 2180'
• 10. 'Product of Thailand'
Nice to have
• Updated logo with company name 'Copper Lantern' and/or company slogan 'Crafted Without Shortcuts' added.
Should not have
• No photos or stock images.
• No elements of the current design (excluding logo) to remain i.e. 'Otter Finn', 'Testosterone Booster', 'Increase Lean Muscle', 'Stabilise Hormones', 'Boost Endurance', 'Improve Muscle Naturally', are all to be omitted.

```html
<!DOCTYPE html>
<html lang="en">
<head>
<meta charset="utf-8">
<title>Copper Lantern – Hormone Support Label</title>
<link rel="stylesheet" href="https://fonts.googleapis.com/css2?family=IBM+Plex+Mono:wght@300;400&family=Montserrat:wght@500&display=swap">
<style>
  :root {
    --backdrop: #cbcac6;
    --label-white: #ffffff;
    --label-shade: #ececec;
    --brand-blue: #2b3aa0;
    --band-blue: #28329a;
    --ink-grey: #3c3c3c;
    --rule-grey: #8a8a8a;
  }
  * { margin: 0; padding: 0; box-sizing: border-box; }
  html, body {
    width: 1200px;
    height: 1200px;
    overflow: hidden;
    background: var(--backdrop);
  }
  .canvas {
    position: relative;
    width: 1200px;
    height: 1200px;
  }
  .bottle-label {
    position: absolute;
    left: 280px;
    top: 110px;
    width: 640px;
    height: 980px;
    background: linear-gradient(90deg, var(--label-shade) 0%, var(--label-white) 18%, var(--label-white) 82%, var(--label-shade) 100%);
    text-align: center;
  }
  .brand-lockup {
    position: absolute;
    top: 70px;
    left: 0;
    width: 100%;
    display: flex;
    flex-direction: column;
    align-items: center;
  }
  .brand-mark {
    width: 150px;
    height: 150px;
    border: 9px solid var(--brand-blue);
    border-radius: 50%;
  }
  .brand-name {
    margin-top: 34px;
    font-family: "Montserrat", sans-serif;
    font-weight: 500;
    font-size: 44px;
    letter-spacing: 4px;
    color: var(--brand-blue);
    text-transform: uppercase;
  }
  .brand-slogan {
    margin-top: 12px;
    font-family: "IBM Plex Mono", monospace;
    font-weight: 400;
    font-size: 18px;
    letter-spacing: 3px;
    color: var(--ink-grey);
    text-transform: uppercase;
  }
  .product-function {
    position: absolute;
    top: 500px;
    left: 0;
    width: 100%;
    font-family: "IBM Plex Mono", monospace;
    font-weight: 400;
    font-size: 50px;
    line-height: 66px;
    letter-spacing: 6px;
    color: var(--brand-blue);
  }
  .rule {
    position: absolute;
    left: 110px;
    width: 420px;
    height: 2px;
    background: linear-gradient(90deg, transparent, var(--rule-grey) 15%, var(--rule-grey) 85%, transparent);
  }
  .rule-top { top: 648px; }
  .rule-bottom { top: 728px; }
  .product-name {
    position: absolute;
    top: 664px;
    left: 0;
    width: 100%;
    font-family: "IBM Plex Mono", monospace;
    font-weight: 400;
    font-size: 32px;
    line-height: 48px;
    letter-spacing: 7px;
    color: var(--ink-grey);
  }
  .volume {
    position: absolute;
    top: 778px;
    left: 0;
    width: 100%;
    font-family: "IBM Plex Mono", monospace;
    font-weight: 400;
    font-size: 34px;
    letter-spacing: 3px;
    color: var(--ink-grey);
  }
  .supplement-type {
    position: absolute;
    top: 838px;
    left: 0;
    width: 100%;
    font-family: "IBM Plex Mono", monospace;
    font-weight: 400;
    font-size: 20px;
    letter-spacing: 5px;
    color: var(--ink-grey);
  }
  .colour-band {
    position: absolute;
    left: 0;
    bottom: 22px;
    width: 100%;
    height: 30px;
    background: var(--band-blue);
  }
</style>
</head>
<body>
  <main class="canvas">
    <section class="bottle-label">
      <div class="brand-lockup">
        <div class="brand-mark"></div>
        <div class="brand-name">Copper Lantern</div>
        <div class="brand-slogan">Crafted Without Shortcuts</div>
      </div>
      <h1 class="product-function">HORMONE<br>SUPPORT</h1>
      <div class="rule rule-top"></div>
      <p class="product-name">JIAOGULAN</p>
      <div class="rule rule-bottom"></div>
      <p class="volume">30ML</p>
      <p class="supplement-type">DIETARY SUPPLEMENT</p>
      <div class="colour-band"></div>
    </section>
  </main>
</body>
</html>
```